Double sided business Card voor Luchtkoel Brederwijk

Card design must be in line with our logo. Clean and professional look. Colors can be used, but not too wild.
Logo in frontside. Details on the backside. We want a qr in the design.

Details: (person)
name: Maarten Bosveld
tel: 06-48271935
maarten@luchtkoelbrederwijk.nl

tel: 088-5063918 (business general)
info@luchtkoelbrederwijk.nl

.

```html
<!DOCTYPE html>
<html lang="nl">
<head>
<meta charset="utf-8">
<title>Luchtkoel Brederwijk – Visitekaartje</title>
<link href="https://fonts.googleapis.com/css2?family=Libre+Franklin:wght@400;700;800&display=swap" rel="stylesheet">
<style>
  :root {
    --brand-blue: #0063b0;
    --ink: #3e3e40;
    --paper: #ffffff;
    --page: #ffffff;
    --shadow: rgba(0, 0, 0, 0.28);
    --qr-tone: #d9dde3;
  }
  * { margin: 0; padding: 0; box-sizing: border-box; }
  html, body {
    width: 965px;
    height: 1200px;
    overflow: hidden;
    background: var(--page);
    font-family: "Libre Franklin", Arial, sans-serif;
    color: var(--ink);
  }
  .sheet { position: relative; width: 965px; height: 1200px; }

  .card {
    position: absolute;
    left: 92px;
    width: 785px;
    height: 471px;
    background: var(--paper);
    box-shadow: 0 0 40px 12px var(--shadow);
  }
  .card--front { top: 77px; }
  .card--back { top: 622px; }
  .card__band {
    position: absolute;
    left: 0; top: 0;
    width: 100%;
    height: 49px;
    background: var(--brand-blue);
  }

  .side-label {
    position: absolute;
    left: 90px;
    font-size: 22px;
    font-weight: 400;
    color: #222;
  }
  .side-label--front { top: 553px; }
  .side-label--back { top: 1102px; }

  /* Front */
  .brand {
    position: absolute;
    left: 0; top: 140px;
    width: 100%;
    text-align: center;
  }
  .brand__mark {
    display: block;
    width: 120px;
    height: 120px;
    margin: 0 auto 38px;
    border-radius: 50%;
    background: var(--brand-blue);
  }
  .brand__name {
    font-size: 30px;
    font-weight: 400;
    letter-spacing: 9px;
    line-height: 40px;
    text-transform: uppercase;
    color: var(--ink);
  }

  /* Back */
  .holder {
    position: absolute;
    left: 20px;
    width: 292px;
    top: 244px;
    text-align: right;
    font-size: 26px;
    font-weight: 800;
    letter-spacing: -0.5px;
    line-height: 32px;
    white-space: nowrap;
    text-transform: uppercase;
    color: var(--ink);
  }
  .divider {
    position: absolute;
    left: 335px;
    top: 144px;
    width: 2px;
    height: 233px;
    background: var(--ink);
  }
  .contact {
    position: absolute;
    left: 360px;
    top: 154px;
    list-style: none;
  }
  .contact__group { margin-bottom: 11px; }
  .contact__label {
    font-size: 20px;
    font-weight: 800;
    line-height: 24px;
  }
  .contact__value {
    font-size: 21px;
    font-weight: 400;
    line-height: 27px;
  }
  .qr {
    position: absolute;
    right: 40px;
    bottom: 24px;
    width: 66px;
    height: 66px;
    background: var(--qr-tone);
  }
</style>
</head>
<body>
<main class="sheet">
  <section class="card card--front" aria-label="Voorkant">
    <div class="card__band"></div>
    <div class="brand">
      <span class="brand__mark" aria-hidden="true"></span>
      <p class="brand__name">Luchtkoel<br>Brederwijk</p>
    </div>
  </section>
  <p class="side-label side-label--front">Front</p>

  <section class="card card--back" aria-label="Achterkant">
    <div class="card__band"></div>
    <h1 class="holder">Maarten Bosveld</h1>
    <div class="divider"></div>
    <ul class="contact">
      <li class="contact__group">
        <p class="contact__label">Phone</p>
        <p class="contact__value">06-48271935</p>
        <p class="contact__value">088-5063918 (Business General)</p>
      </li>
      <li class="contact__group">
        <p class="contact__label">Email</p>
        <p class="contact__value">maarten@luchtkoelbrederwijk.nl</p>
      </li>
      <li class="contact__group">
        <p class="contact__label">Web</p>
        <p class="contact__value">www.info@luchtkoelbrederwijk.nl</p>
      </li>
    </ul>
    <div class="qr" role="img" aria-label="Plaats voor QR-code naar de website"></div>
  </section>
  <p class="side-label side-label--back">Back</p>
</main>
</body>
</html>
```